Book Cover for Content Marketing Design Process that Targets Creative Entreprenuers

Book Cover for Kindle and print. I like the design I have which I attached, but want the professional touch. The book takes readers through a 3-day creative process to design a written content management strategy for their product or service. It's very experiential, and uses a playful guiding metaphor throughout. Despite the playful non-linear approach, the result is a very comprehensive and practical content plan that puts value and authentic service to customers first.

The message the cover should convey is that it's possible for the business owner to attract the attention of customers, to generate excitement, and to connect with an audience on an emotional level. I estimate the book spine to be around 0.30" on a 6" x 9" cover. For Kindle, the imaged needs to be 2,560 x 1,600 JPG format, no more than 50MB.

Target Market(s)

Creative entrepreneurs, artists, artisans who sell online.

Industry/Entity Type

Consulting

Requirements
Must have
• This is a very creative, spiritual, energetic approach to content marketing. I would like the cover to set the stage for the experiential and creative process to come. Should appear bold and fun.
Nice to have
• What I like about the file attached: the expressive faces highlighting the idea of getting attention and attracting an audience, the playful font for "Playbook," the color scheme. I think the subtitle is important, but not sure if it should be on the cover or not.
Should not have
• Nothing that veers into child-like.

```html
<!DOCTYPE html>
<html lang="en">
<head>
<meta charset="utf-8">
<title>Content Marketing Playbook — Book Cover</title>
<link rel="stylesheet" href="https://fonts.googleapis.com/css2?family=Fjalla+One&family=Dancing+Script:wght@700&family=Montserrat:wght@500;700&display=swap">
<style>
  :root {
    --backdrop: #e1e1e1;
    --paper: #ffffff;
    --navy: #0f4a86;
    --band-dark: #0b2a4e;
    --band-light: #3a8fd0;
    --crimson: #9a1628;
    --rule: #b9c7d8;
  }
  * { margin: 0; padding: 0; box-sizing: border-box; }
  html, body { width: 1200px; height: 900px; overflow: hidden; background: var(--backdrop); }
  .cover {
    position: absolute; left: 310px; top: 0; width: 638px; height: 900px;
    background: var(--paper); overflow: hidden;
  }
  .band { position: absolute; left: 0; width: 100%; height: 12px; }
  .band--top { top: 4px; }
  .band--bottom { top: 880px; }
  .photo { position: absolute; }
  .photo--one { left: 0; top: 363px; width: 172px; height: 188px; }
  .photo--two { left: 112px; top: 464px; width: 195px; height: 184px; }
  .photo--three { left: 297px; top: 424px; width: 191px; height: 197px; }
  .photo--four { left: 30px; top: 640px; width: 180px; height: 180px; transform: rotate(-17deg); }
  .type-layer { position: absolute; left: 0; top: 0; width: 638px; height: 900px; pointer-events: none; }
  .title-block { font-family: "Fjalla One", "Arial Narrow", sans-serif; fill: var(--navy); }
  .title-content { font-size: 118px; }
  .title-marketing { font-size: 90px; }
  .title-playbook { font-family: "Dancing Script", cursive; font-size: 132px; fill: var(--crimson); }
  .subtitle { font-family: "Montserrat", sans-serif; font-weight: 700; font-size: 24px; fill: var(--navy); }
  .tagline { font-family: "Fjalla One", "Arial Narrow", sans-serif; font-size: 20px; fill: var(--navy); }
  .tagline .accent { fill: var(--crimson); }
  .author { font-family: "Montserrat", sans-serif; font-weight: 500; font-size: 30px; fill: var(--navy); }
</style>
</head>
<body>
<main class="cover">
  <svg class="band band--top" viewBox="0 0 638 12" preserveAspectRatio="none" aria-hidden="true">
    <rect width="638" height="4" fill="var(--band-dark)"/>
    <rect y="4" width="638" height="4" fill="var(--band-light)"/>
    <rect y="8" width="638" height="4" fill="var(--band-dark)"/>
  </svg>

  <div class="photo photo--one" role="img" aria-label="Close-up portrait of a calm woman with dark curly hair" style="background: linear-gradient(160deg, #5a3a2a, #a9725a 55%, #3b2418);"></div>
  <div class="photo photo--two" role="img" aria-label="Portrait of a woman with dark bob hair and red nails touching her cheek" style="background: linear-gradient(150deg, #2a1c18, #e6c4b4 50%, #f3ddd3);"></div>
  <div class="photo photo--three" role="img" aria-label="Excited woman with curly red hair raising her hands beside her face" style="background: linear-gradient(180deg, #e9e9e9, #c99a7e 45%, #8b7a6a);"></div>
  <div class="photo photo--four" role="img" aria-label="Smiling young woman with face paint dots against a soft pink background" style="background: linear-gradient(135deg, #f3a07a, #e8b9a2 50%, #b65a4a);"></div>

  <svg class="type-layer" viewBox="0 0 638 900">
    <defs>
      <linearGradient id="tagline-rule" x1="0" x2="1" y1="0" y2="0">
        <stop offset="0" stop-color="var(--rule)" stop-opacity="0"/>
        <stop offset="0.5" stop-color="var(--rule)"/>
        <stop offset="1" stop-color="var(--rule)" stop-opacity="0"/>
      </linearGradient>
    </defs>
    <g class="title-block">
      <text class="title-content" x="68" y="132" textLength="457" lengthAdjust="spacingAndGlyphs">CONTENT</text>
      <text class="title-marketing" x="68" y="212" textLength="457" lengthAdjust="spacingAndGlyphs">MARKETING</text>
    </g>
    <text class="title-playbook" x="62" y="298" textLength="450" lengthAdjust="spacingAndGlyphs">Playbook</text>
    <text class="subtitle" x="64" y="360" textLength="461" lengthAdjust="spacingAndGlyphs">AND STRAIGHT FROM THE HEART</text>

    <rect x="210" y="665" width="290" height="2" fill="url(#tagline-rule)"/>
    <text class="tagline" x="207" y="692" textLength="298" lengthAdjust="spacingAndGlyphs">ATTRACT MORE <tspan class="accent">ATTENTION</tspan> ONLINE</text>
    <text class="tagline" x="239" y="716" textLength="234" lengthAdjust="spacingAndGlyphs">WITH A CONTENT STRATEGY</text>
    <text class="tagline" x="257" y="740"><tspan class="accent" textLength="198" lengthAdjust="spacingAndGlyphs">THAT’S FUN, MAGNETIC</tspan></text>
    <rect x="240" y="748" width="260" height="2" fill="url(#tagline-rule)"/>

    <text class="author" x="166" y="852" textLength="297" lengthAdjust="spacing">AUTHOR NAME</text>
  </svg>

  <svg class="band band--bottom" viewBox="0 0 638 12" preserveAspectRatio="none" aria-hidden="true">
    <rect width="638" height="4" fill="var(--band-dark)"/>
    <rect y="4" width="638" height="4" fill="var(--band-light)"/>
    <rect y="8" width="638" height="4" fill="var(--band-dark)"/>
  </svg>
</main>
</body>
</html>
```